Quiet Summit Podcast W/ Dr. Lena Voss

Podcast Cover Art. I am in search of a re-design for my existing podcast. We have over 100 episodes, but I want to change the name to Quiet Summit Podcast With Dr. Lena Voss. I'm open to any ideas, and have attached source file image to use. ( note: NO brain images please).

```html
<!DOCTYPE html>
<html lang="en">
<head>
<meta charset="utf-8">
<title>Quiet Summit Podcast – Cover Art</title>
<link rel="stylesheet" href="https://fonts.googleapis.com/css2?family=Bebas+Neue&family=Poppins:wght@400&display=swap">
<style>
  :root {
    --red-light: #d73b2c;
    --red-deep: #b3281f;
    --band-light: #ededed;
    --bar-dark: #3b0a04;
    --ink: #ffffff;
    --ink-dark: #1e1e1e;
    --host-orange: #e4553a;
    --host-orange-deep: #c43d27;
  }
  * { margin: 0; padding: 0; box-sizing: border-box; }
  html, body { width: 1200px; height: 1200px; overflow: hidden; background: var(--band-light); }
  .cover {
    position: relative;
    width: 1200px;
    height: 1200px;
    overflow: hidden;
    background: var(--band-light);
    font-family: "Bebas Neue", "Arial Narrow", sans-serif;
  }
  .cover__field {
    position: absolute;
    left: 0; top: 0;
    width: 1200px; height: 739px;
    background: linear-gradient(135deg, var(--red-light) 0%, var(--red-deep) 100%);
  }
  .cover__name-bar {
    position: absolute;
    left: 0; top: 758px;
    width: 913px; height: 243px;
    background: var(--bar-dark);
  }
  .title {
    position: absolute;
    left: 60px;
    color: var(--ink);
    line-height: 1;
    white-space: nowrap;
    text-transform: uppercase;
    font-weight: 400;
  }
  .title--primary { top: 58px; font-size: 445px; letter-spacing: 6px; }
  .title--secondary { top: 431px; font-size: 245px; letter-spacing: 22px; }
  .host-name {
    position: absolute;
    left: 60px; top: 806px;
    color: var(--ink);
    font-size: 150px;
    line-height: 1;
    letter-spacing: 2px;
    white-space: nowrap;
    text-transform: uppercase;
  }
  .show-label {
    position: absolute;
    left: 58px; top: 1044px;
    font-family: "Poppins", "Helvetica", sans-serif;
    font-size: 40px;
    line-height: 1;
    letter-spacing: 8px;
    color: var(--ink-dark);
    text-transform: uppercase;
  }
  .host-portrait {
    position: absolute;
    left: 636px; top: 440px;
    width: 564px; height: 760px;
  }
</style>
</head>
<body>
<main class="cover">
  <div class="cover__field"></div>
  <div class="cover__name-bar"></div>

  <h1 class="title title--primary">Quiet</h1>
  <p class="title title--secondary">Summit</p>

  <p class="host-name">Dr. Lena Voss</p>
  <p class="show-label">Podcast</p>

  <svg class="host-portrait" viewBox="0 0 564 760" role="img" aria-label="Illustrated portrait of the host, Dr. Lena Voss, in an orange plaid blazer">
    <defs>
      <linearGradient id="hostFill" x1="0" y1="0" x2="0" y2="1">
        <stop offset="0" stop-color="var(--host-orange)"/>
        <stop offset="1" stop-color="var(--host-orange-deep)"/>
      </linearGradient>
    </defs>
    <path fill="url(#hostFill)" d="M250 0 C350 0 410 70 412 170 C414 260 400 330 370 360 L380 380 C450 410 530 440 564 470 L564 760 L0 760 C0 650 20 560 60 500 C100 450 170 410 190 380 L200 360 C170 330 160 260 162 170 C164 70 180 0 250 0 Z"/>
  </svg>
</main>
</body>
</html>
```